Innovative IT Service Provider seeks engaging overview presentation to capture new business

*Please see attached Creative Brief for full details*

Overall Goals
The goal of this presentation is to provide new, prospective clients with an introduction to Harborline Systems, the services we provide, and what makes us a unique and superior choice for their IT Services. The deck should be able to clearly relay this information while clients review it on their own, without further explanation from a company representative.

Design Goals
We are looking for a professional, modern, streamlined, sleek design that reflects our status as a leader in information technology and innovation.

Company Overview
As an IT Managed Service Provider, companies choose to outsource some or all of their internal IT functions to us to take advantage of our many areas of expertise and so they can focus on their core business, whatever industry they may be in. We also specialize in IT Cyber Security and Consulting, always providing our clients with thought leadership and insight into the latest IT innovations. We ultimately find ways to deliver value to our clients through our various IT solutions.

```html
<!DOCTYPE html>
<html lang="en">
<head>
<meta charset="utf-8">
<title>Harborline Systems – Measured, Managed &amp; Mature</title>
<link href="https://fonts.googleapis.com/css2?family=Arimo:wght@400;700&display=swap" rel="stylesheet">
<style>
  :root {
    --band: #d9d9d9;
    --navy: #1c3a6b;
    --ink: #222222;
    --panel-border: #111111;
    --dash-navy: #2b3f6b;
    --dash-blue: #3b6fc4;
    --dash-light: #b9d2ee;
    --dash-grey: #8a8a8a;
    --dash-line: #d6d6d6;
    --red: #c8323c;
    --white: #ffffff;
  }
  * { box-sizing: border-box; margin: 0; padding: 0; }
  html, body { width: 1200px; height: 675px; overflow: hidden; background: var(--white); }
  body { font-family: "Arimo", Arial, sans-serif; color: var(--ink); }
  .slide { position: relative; width: 1200px; height: 675px; overflow: hidden; background: var(--white); }

  .top-band { position: absolute; left: 0; top: 0; width: 1200px; height: 87px; background: var(--band); }
  .brand { position: absolute; left: 30px; top: 24px; display: flex; align-items: center; gap: 12px; }
  .brand-square { width: 34px; height: 34px; background: var(--navy); }
  .brand-name { font-size: 22px; font-weight: 700; color: var(--navy); letter-spacing: 0.5px; }
  .bottom-band { position: absolute; left: 0; top: 603px; width: 1200px; height: 72px; background: var(--band); }

  .slide-title { position: absolute; left: 36px; top: 112px; font-size: 28px; font-weight: 700; color: var(--navy); }
  .checklist { position: absolute; left: 47px; top: 202px; list-style: none; }
  .checklist li { font-size: 24px; height: 72px; line-height: 36px; }
  .checklist li::before { content: "\2713"; margin-right: 12px; }

  .dash { position: absolute; background: var(--white); border: 3px solid var(--panel-border); box-shadow: 4px 5px 8px rgba(0,0,0,0.35); overflow: hidden; font-size: 7px; color: #444; }
  .dash-calls { left: 520px; top: 136px; width: 480px; height: 322px; }
  .dash-survey { left: 636px; top: 208px; width: 448px; height: 243px; }
  .dash-tickets { left: 750px; top: 300px; width: 428px; height: 273px; }

  .dash-header { height: 20px; background: var(--dash-navy); color: var(--white); font-size: 11px; font-style: italic; text-align: center; line-height: 20px; }
  .lbl { position: absolute; font-size: 7px; line-height: 1.2; color: #444; }
  .big { position: absolute; font-size: 30px; color: #333; }
  .mini-table { position: absolute; border-collapse: collapse; font-size: 6px; }
  .mini-table td, .mini-table th { border-bottom: 1px solid var(--dash-line); padding: 2px 4px; font-weight: 400; text-align: left; }
  .mini-table .hi { background: var(--dash-light); }
  .survey-tag { position: absolute; left: 10px; top: 8px; width: 100px; height: 22px; background: var(--dash-navy); color: var(--white); font-size: 11px; font-style: italic; line-height: 22px; padding-left: 8px; }
  .bar { position: absolute; height: 6px; background: var(--dash-light); }
  .pie { position: absolute; border-radius: 50%; }
  .pie-left { left: 30px; top: 140px; width: 92px; height: 92px;
    background: conic-gradient(#2a3f7a 0 22%, #c8323c 22% 34%, #5b8fd6 34% 52%, #9aa3b5 52% 64%, #1f6fb0 64% 80%, #7a2433 80% 100%); }
  .pie-right { left: 264px; top: 138px; width: 100px; height: 100px;
    background: conic-gradient(#5bb0c8 0 18%, #c8323c 18% 30%, #f08a8a 30% 44%, #2a3f7a 44% 60%, #9ac7e6 60% 76%, #e6b3b3 76% 100%); }
  .legend { position: absolute; list-style: none; font-size: 6px; }
  .legend li { height: 9px; display: flex; align-items: center; gap: 3px; }
  .legend i { display: inline-block; width: 5px; height: 5px; border-radius: 50%; }
</style>
</head>
<body>
<div class="slide">
  <div class="top-band">
    <div class="brand"><span class="brand-square"></span><span class="brand-name">HARBORLINE SYSTEMS</span></div>
  </div>

  <h1 class="slide-title">Measured, Managed &amp; Mature</h1>
  <ul class="checklist">
    <li>Business Analytics</li>
    <li>Trend Analysis</li>
    <li>Continuous Improvement</li>
  </ul>

  <!-- Calls dashboard -->
  <section class="dash dash-calls">
    <div class="dash-header">Calls</div>
    <div class="lbl" style="left:10px;top:34px;width:90px;">Abandon Rate Previous Month</div>
    <svg style="position:absolute;left:12px;top:64px" width="120" height="66" viewBox="0 0 120 66">
      <path d="M10 60 A50 50 0 0 1 110 60" fill="none" stroke="#e3e3e3" stroke-width="14"/>
      <path d="M10 60 A50 50 0 0 1 12 46" fill="none" stroke="var(--dash-blue)" stroke-width="14"/>
      <text x="60" y="58" font-size="13" text-anchor="middle" fill="#444" font-family="Arimo, sans-serif">2.00%</text>
    </svg>
    <div class="lbl" style="left:160px;top:34px;width:110px;">Answered within 2 Minutes Rate Previous Month</div>
    <svg style="position:absolute;left:160px;top:60px" width="110" height="60" viewBox="0 0 110 60">
      <path d="M8 56 A47 47 0 0 1 102 56" fill="none" stroke="var(--dash-navy)" stroke-width="14"/>
    </svg>
    <table class="mini-table" style="left:290px;top:30px;width:180px;">
      <tr><th>Day</th><th>Answered</th><th>Missed</th><th>Long</th><th>Rate</th></tr>
      <tr><td>1</td><td>42</td><td>1</td><td>0</td><td>2%</td></tr>
    </table>
    <div class="lbl" style="left:10px;top:206px;width:100px;">ASA Seconds Previous Month</div>
    <div class="big" style="left:34px;top:228px;">15</div>
    <div class="lbl" style="left:24px;top:266px;">Average Speed of Answer</div>
  </section>

  <!-- Survey dashboard -->
  <section class="dash dash-survey">
    <div class="survey-tag">Survey Results</div>
    <div class="lbl" style="left:14px;top:40px;"><b>Answered All</b></div>
    <div class="lbl" style="left:14px;top:50px;">■ Not Answered</div>
    <div class="lbl" style="left:152px;top:6px;width:100px;">Survey Result Average Rating Previous Month</div>
    <div class="big" style="left:160px;top:32px;">4.65</div>
    <div class="lbl" style="left:166px;top:68px;">Average of Rating</div>
    <div class="lbl" style="left:262px;top:6px;width:100px;">Count Survey Results Previous Month</div>
    <div class="big" style="left:276px;top:32px;">33</div>
    <div class="lbl" style="left:272px;top:68px;">Count of Results</div>
    <table class="mini-table" style="left:342px;top:10px;width:98px;">
      <tr><th>Team</th><th>Avg</th><th>Score</th><th>Count</th></tr>
      <tr><td>A</td><td class="hi">4.7</td><td class="hi">92</td><td class="hi">12</td></tr>
      <tr><td>B</td><td class="hi">4.6</td><td class="hi">90</td><td class="hi">11</td></tr>
      <tr><td>C</td><td class="hi">4.6</td><td class="hi">91</td><td class="hi">10</td></tr>
    </table>
    <div class="lbl" style="left:180px;top:94px;">Average Points per Question</div>
    <div class="lbl" style="left:14px;top:112px;">Q1</div><div class="bar" style="left:40px;top:112px;width:360px;"></div>
    <div class="lbl" style="left:14px;top:124px;">Q2</div><div class="bar" style="left:40px;top:124px;width:330px;"></div>
    <div class="lbl" style="left:14px;top:136px;">Q3</div><div class="bar" style="left:40px;top:136px;width:345px;"></div>
    <div class="lbl" style="left:14px;top:164px;width:100px;">Handling Advisory Previous Month</div>
    <div class="big" style="left:12px;top:184px;font-size:26px;">99.50%</div>
    <div class="lbl" style="left:34px;top:218px;">Handling Rate</div>
  </section>

  <!-- Tickets dashboard -->
  <section class="dash dash-tickets">
    <div class="lbl" style="left:10px;top:18px;">Tickets by Month and Status</div>
    <div style="position:absolute;left:40px;top:34px;width:16px;height:90px;background:var(--dash-light);"></div>
    <div style="position:absolute;left:40px;top:70px;width:16px;height:6px;background:var(--red);"></div>
    <ul class="legend" style="left:72px;top:40px;">
      <li><i style="background:var(--dash-navy)"></i>Open</li>
      <li><i style="background:var(--dash-blue)"></i>Closed</li>
      <li><i style="background:var(--red)"></i>Pending</li>
    </ul>
    <div style="position:absolute;left:160px;top:30px;width:70px;height:80px;border:1px solid var(--dash-line);"></div>
    <div style="position:absolute;left:250px;top:30px;width:150px;height:80px;border:1px solid var(--dash-line);"></div>
    <div style="position:absolute;left:270px;top:64px;width:80px;height:10px;background:var(--dash-navy);"></div>
    <div class="lbl" style="left:20px;top:128px;">Tickets by Type</div>
    <div class="pie pie-left" role="img" aria-label="Pie chart of tickets by type"></div>
    <ul class="legend" style="left:140px;top:150px;">
      <li><i style="background:#2a3f7a"></i>Network</li>
      <li><i style="background:#c8323c"></i>Email</li>
      <li><i style="background:#5b8fd6"></i>Access</li>
      <li><i style="background:#9aa3b5"></i>Hardware</li>
      <li><i style="background:#1f6fb0"></i>Software</li>
      <li><i style="background:#7a2433"></i>Other</li>
    </ul>
    <div class="lbl" style="left:262px;top:126px;">Tickets by Category</div>
    <div class="pie pie-right" role="img" aria-label="Pie chart of tickets by category"></div>
    <ul class="legend" style="left:372px;top:150px;">
      <li><i style="background:#5bb0c8"></i>Network</li>
      <li><i style="background:#c8323c"></i>Email</li>
      <li><i style="background:#f08a8a"></i>Access</li>
      <li><i style="background:#2a3f7a"></i>Hardware</li>
      <li><i style="background:#9ac7e6"></i>Software</li>
      <li><i style="background:#e6b3b3"></i>Other</li>
    </ul>
  </section>

  <div class="bottom-band"></div>
</div>
</body>
</html>
```